Business Card Design

Stronger Living Compact for the Plains is a partnership of twenty different health organisations in the western suburbs of Melbourne, working together to improve the health of the local community. The western suburbs of Melbourne is one of the fastest growing and most culturally diverse populations in Australia and its communities have some of the poorest health outcomes in Australia.
Please see location for copy of the SLCP:
http://kvrt.com.au/fileadmin/filemount/pdf_files/SLCFTP_13_FINAL_JUNE_2012.pdf

Reason: Hello. I've extended the deadline because in the brief I made a confusing mention about a logo, but I actually meant the 'Stronger Living Compact for the Plains' jpg that I had already attached. Sorry about the confusion Thanks Fiona

Hello, Thanks for the designs I have already received. I have extended the deadline because I made a confusing reference to a logo in my brief, but I was talking about the 'Stronger Living Compact for the Plains' jpg I had already attached. There is no other logo for me to provide.

Thanks, Fiona

Target Market(s)

Health and state/local government managers and CEOs

Industry/Entity Type

Health

Contact Information for Business Card

Fiona Tremblay
Executive Officer
Stronger Living Compact for the Plains
Ph: 0438 592 614
Fiona.Tremblay@qn.org.au

Requirements
Must have
• logo and details as provided.
Would prefer matt finish
I can't see that logo has successfully attached so if it has not, please email or call me to follow up.

```html
<!DOCTYPE html>
<html lang="en">
<head>
<meta charset="utf-8">
<title>Stronger Living Compact for the Plains – Business Card</title>
<link rel="stylesheet" href="https://fonts.googleapis.com/css2?family=Ubuntu:wght@300;400;700&display=swap">
<style>
  :root {
    --bg: #dcd8d1;
    --blue: #0a8fd4;
    --lime: #b6d55c;
    --white: #ffffff;
    --ink: #1d3346;
    --paper: #fbfbfa;
  }
  * { box-sizing: border-box; margin: 0; padding: 0; }
  html, body {
    width: 1200px; height: 884px; overflow: hidden;
    background: var(--bg);
    font-family: "Ubuntu", Arial, sans-serif;
  }
  .stage {
    width: 1200px; height: 884px;
    display: flex; align-items: center; justify-content: center; gap: 48px;
  }
  .card {
    width: 540px; height: 300px; position: relative; overflow: hidden;
    box-shadow: 0 2px 6px rgba(0,0,0,.12);
  }
  /* Front */
  .card-front { background: var(--lime); }
  .front-panel {
    position: absolute; top: 16px; left: 24px; right: 0; bottom: 40px;
    background: var(--blue);
  }
  .wordmark {
    position: absolute; left: 34px; top: 30px; width: 320px;
    color: var(--white); font-weight: 700; font-size: 40px; line-height: 1.0;
    letter-spacing: -0.5px;
  }
  /* Back */
  .card-back { background: var(--paper); }
  .contact { position: absolute; left: 40px; top: 40px; right: 40px; }
  .contact-name { color: var(--blue); font-size: 30px; font-weight: 400; }
  .contact-role { color: var(--ink); font-size: 20px; font-weight: 400; margin-top: 2px; }
  .rule { height: 2px; background: var(--blue); width: 300px; margin-top: 30px; }
  .contact-details {
    margin-top: 12px; color: var(--blue); font-size: 14px; line-height: 1.45;
  }
  .back-band {
    position: absolute; left: 0; right: 0; bottom: 0; height: 44px;
    background: var(--blue); border-top: 5px solid var(--lime);
    display: flex; align-items: center; justify-content: flex-end;
    padding-right: 28px;
  }
  .band-name {
    color: var(--white); font-size: 12px; font-weight: 700;
    letter-spacing: 1px; text-transform: uppercase;
  }
</style>
</head>
<body>
  <main class="stage">
    <section class="card card-front" aria-label="Business card front">
      <div class="front-panel">
        <p class="wordmark">Stronger Living Compact for the Plains</p>
      </div>
    </section>

    <section class="card card-back" aria-label="Business card back">
      <div class="contact">
        <h1 class="contact-name">Fiona Tremblay</h1>
        <p class="contact-role">Executive Officer</p>
        <div class="rule"></div>
        <p class="contact-details">
          Ph: 0438 592 614<br>
          Fiona.Tremblay@qn.org.au
        </p>
      </div>
      <div class="back-band">
        <span class="band-name">Stronger Living Compact for the Plains</span>
      </div>
    </section>
  </main>
</body>
</html>
```